Large corporation needs landing page for its employees with emotional and psychological problems

Vision:
Hello, we are a startup and would like to build a landing page and website in the mental health sector for a large corporation. In this site employees with emotional and psychological problems should quickly receive professional psychological support. This support takes the form of internal referrals from employees who are looking for help to qualified therapists, so that help can be provided quickly.
Furthermore, the employees get access to a tool where they can find out about topics in the mind health area and can also get help via webinars and podcasts. The employee should thus be able to take the hurdle to seek help and support in good time.
Therapists for whom the focus is on the urgency of providing quick help and support will work here in cooperation with the respective corporations.
Keywords:
• Help/Support
• overcome inhibitions
• Competent help
• Uncomplicated help
• Permanent access
• protected space
• Recognizing and naming emotional problems and actively tackling them
• get help
• mindfulness
• everyday helper
• Informative
• Anonymous
• compassion
• tolerance
• respect
• Appreciation
• empathy
• mindfulness
• protected space
• To be needed
• Like a lighthouse signal
What we need:
Landingpage
We need a landing page aimed at getting employees to contact psychological help. The call to action is to get in contact via a contact form.
Landing page content
There are several text modules:
• A heading/greeting
• A body of text at the beginning that explains the purpose of the page
• A bulleted text area describing the pain points and the solutions to them
Video:
The heart of the content will be a video explaining the need and inviting them to get in touch.
contact form:
It should be kept simple: first name, last name and email address
Legally required content:
General terms and conditions, data protection and imprint. These are only given as links in the footer.
In parallel, the Corporate Design should be adapted/extended:
Logo:
The font in the logo should be revised. The wings in the background remain.
Please adapt the logo for different uses:
• on a black background
• with transparent background
• favorite icon (browser)
• In square format for social media
Colors:
• develop a color chart based on the colors of the logo.
• please determine 2-3 main colors and the matching variations. I.e. transparent variations or light colors.
Typography:
Determine a decorative font and/or typography for headings and a text font. There should be no more than 3 fonts.
Updates
Need extra days to review
Industry/Entity Type
to recruit therapists as employees
Should not have
- please not to playful design or typography - and max. 3 colors

```html
<!DOCTYPE html>
<html lang="en">
<head>
<meta charset="utf-8">
<title>Calm Harbor — Professional Psychological Support</title>
<link href="https://fonts.googleapis.com/css2?family=Archivo:wght@600;700;800;900&family=Inter:wght@400;500;600;700&display=swap" rel="stylesheet">
<style>
:root{
  --teal:#0b5566;
  --teal-mid:#0f6a7c;
  --ink:#1b2a31;
  --text:#3a4348;
  --hero:#b4dbe5;
  --pale:#e6f3f8;
  --footer:#23263a;
  --white:#ffffff;
  --muted:#9aa1b2;
}
*{box-sizing:border-box;margin:0;padding:0}
html,body{width:1200px;height:4844px;overflow:hidden}
body{position:relative;background:var(--white);font-family:"Inter",sans-serif;color:var(--text)}
.abs{position:absolute}
h1,h2,h3{font-family:"Archivo",sans-serif;color:var(--ink)}
/* header */
.brand{left:96px;top:22px;font-family:"Archivo",sans-serif;font-weight:700;font-size:36px;color:var(--teal);letter-spacing:-0.5px}
.social{display:flex;gap:6px}
.social span{width:32px;height:32px;border:2px solid var(--teal);border-radius:5px;display:block}
.social.top{left:797px;top:24px}
.phone-pill{left:935px;top:22px;width:165px;height:36px;background:var(--teal);border-radius:18px 4px 4px 18px;color:#fff;font-weight:600;font-size:16px;display:flex;align-items:center;gap:12px;padding-left:2px}
.phone-pill .ico{width:34px;height:34px;border-radius:50%;background:#fff;display:flex;align-items:center;justify-content:center}
/* hero */
.hero{left:0;top:83px;width:1200px;height:560px;background:var(--hero);overflow:hidden}
.hero-tag{left:100px;top:230px;font-size:14px;color:var(--ink)}
.hero-title{left:100px;top:262px;font-weight:900;font-size:53px;line-height:62px;letter-spacing:0.5px}
.brain{left:613px;top:150px;width:387px;height:493px;border-radius:48% 46% 0 0;background:radial-gradient(ellipse at 40% 40%,#5a5f64,#222528 70%)}
.badge{left:871px;top:154px;width:197px;height:64px;background:var(--teal-mid);border-radius:10px;color:#fff;display:flex;align-items:center;gap:14px;padding-left:16px}
.badge small{display:block;font-size:12px;color:#cfe9ef}
.badge b{font-size:17px}
.pager{left:97px;top:576px;display:flex;align-items:center;gap:18px}
.pager i{width:6px;height:6px;border-radius:50%;background:#6e98a3;display:block}
/* about */
.eyebrow{left:100px;top:763px;font-size:14px;font-weight:700;color:var(--teal)}
.about-title{left:100px;top:785px;font-size:50px;font-weight:800}
.about-text{left:100px;top:868px;width:490px;font-size:15.5px;line-height:26.7px}
.help{left:700px;top:767px;width:400px;height:377px;background:var(--teal);border-radius:4px;padding:42px 24px 0}
.help h3{color:#fff;font-size:32px;font-weight:800;margin-bottom:16px}
.field{width:350px;height:44px;background:#fff;border-radius:4px;margin-bottom:11px;font-size:15px;color:#333;padding:13px 8px}
.submit{margin-top:12px;width:136px;height:45px;border:2px solid #fff;border-radius:6px;color:#fff;font-weight:700;font-size:16px;display:flex;align-items:center;justify-content:center}
/* offer */
.offer{left:0;top:1266px;width:1200px;height:833px;background:var(--pale)}
.offer-title{left:0;top:1333px;width:1200px;text-align:center;font-size:53px;font-weight:800}
.offer-sub{left:180px;top:1403px;width:840px;text-align:center;font-size:15.5px;line-height:27px;color:var(--ink)}
.service{width:320px;text-align:center}
.service .pic{width:100px;height:98px;margin:0 auto;border-radius:50%;background:radial-gradient(circle,#bfe0e8,#e6f3f8 72%)}
.service h4{font-size:19px;font-weight:600;color:var(--ink);margin:16px 0 14px}
.service p{font-size:15.5px;line-height:26.5px}
/* who */
.who-title{left:98px;top:2210px;font-size:50px;font-weight:800}
.who-text{left:98px;top:2285px;width:490px;font-size:15.5px;line-height:26.7px}
.stats{left:98px;top:2423px;width:542px;height:117px;background:#fff;border-radius:10px;box-shadow:0 8px 30px rgba(0,40,60,.12);display:flex;align-items:center;z-index:2}
.stat{flex:1;text-align:center;border-right:1px solid #dde4e7}
.stat:last-child{border-right:none}
.stat b{display:block;font-family:"Archivo",sans-serif;font-size:46px;font-weight:600;color:var(--teal);line-height:50px}
.stat span{font-size:14px;color:var(--ink)}
.photo{border-radius:4px}
/* video */
.video{left:100px;top:2703px;width:997px;height:500px;background:linear-gradient(180deg,#8c8e73 0%,#6f7a72 30%,#b7a98d 60%,#d9c2a3 100%);box-shadow:0 18px 30px rgba(0,0,0,.18)}
/* benefits */
.ben-title{left:100px;top:3392px;font-size:53px;font-weight:800;line-height:58px}
.ben-title em{font-style:normal;color:var(--teal)}
.ben-list{left:100px;top:3530px;width:470px;list-style:none;font-size:15.5px;font-weight:600;color:var(--ink);line-height:26px}
.ben-list li{position:relative;padding-left:18px;margin-bottom:9px}
.ben-list li::before{content:"";position:absolute;left:0;top:10px;width:7px;height:7px;border-radius:50%;background:var(--teal)}
/* testimonial */
.quote-card{left:482px;top:3905px;width:613px;height:374px;background:#fff;border-radius:18px;box-shadow:0 8px 30px rgba(0,40,60,.12);padding:40px 36px}
.quote-card h3{font-family:"Inter",sans-serif;font-weight:500;font-size:40px;margin:14px 0 14px}
.quote-card p{font-size:22px;line-height:33px;color:var(--ink)}
.person{display:flex;align-items:center;gap:16px;margin-top:26px}
.avatar{width:68px;height:68px;border-radius:50%;background:linear-gradient(#b9c4e9,#8d9bd2)}
.person b{display:block;color:var(--teal);font-size:19px}
.person small{font-size:13px;color:var(--ink)}
/* footer */
.footer{left:0;top:4428px;width:1200px;height:416px;background:var(--footer)}
.f-brand{left:98px;top:4513px;font-family:"Archivo",sans-serif;font-weight:700;font-size:44px;color:var(--teal-mid)}
.f-text{left:98px;top:4591px;width:300px;font-size:15.5px;line-height:26.7px;color:var(--muted)}
.social.foot{left:98px;top:4721px}
.social.foot span{width:40px;height:40px;border-color:#fff}
.f-links-title{left:474px;top:4544px;color:#fff;font-weight:600;font-size:20px}
.f-links{left:474px;top:4590px;list-style:none;font-size:15.5px;color:var(--muted);line-height:45px}
.f-links li::before{content:"› ";color:var(--teal-mid)}
.f-rule{left:98px;top:4787px;width:642px;height:1px;background:#3b3f55}
.copy{left:98px;top:4810px;font-size:14px;color:var(--muted)}
.copy b{color:#fff;font-weight:600}
.meditate{left:677px;top:4336px;width:523px;height:442px;border-radius:50% 50% 40% 40%;background:radial-gradient(ellipse at 50% 40%,#d9c7b3,#9fb9cf 60%,rgba(35,38,58,0) 72%)}
</style>
</head>
<body>

<!-- header -->
<div class="abs brand">Calm Harbor</div>
<div class="abs social top" aria-label="Social links"><span></span><span></span><span></span></div>
<div class="abs phone-pill"><span class="ico"><svg width="16" height="16" viewBox="0 0 24 24"><path fill="#0b5566" d="M6.6 10.8a15 15 0 006.6 6.6l2.2-2.2c.3-.3.7-.4 1-.2 1.1.4 2.3.6 3.6.6.6 0 1 .4 1 1V20c0 .6-.4 1-1 1A17 17 0 013 4c0-.6.4-1 1-1h3.5c.6 0 1 .4 1 1 0 1.3.2 2.5.6 3.6.1.3 0 .7-.2 1z"/></svg></span>1800 555 010</div>

<!-- hero -->
<section class="abs hero">
  <svg class="abs" style="left:0;top:0" width="1200" height="560" viewBox="0 0 1200 560"><path d="M520 260 C700 220 820 300 1200 300 L1200 330 C900 320 760 260 520 260Z" fill="#d6eef3" opacity=".7"/><path d="M1040 320 C1100 300 1160 320 1200 310 L1200 330 C1150 335 1090 330 1040 320Z" fill="#eaf6f9"/></svg>
</section>
<div class="abs hero-tag">Emotional and psychological problems should quickly receive</div>
<h1 class="abs hero-title">PROFESSIONAL<br>PSYCHOLOGICAL<br>SUPPORT</h1>
<div class="abs brain" role="img" aria-label="Sculpted brain with a teal overlay"></div>
<div class="abs" style="left:747px;top:346px;width:253px;height:297px;background:rgba(60,170,190,.45)"></div>
<div class="abs badge"><svg width="30" height="30" viewBox="0 0 24 24" fill="none" stroke="#fff" stroke-width="2"><circle cx="12" cy="12" r="10"/><path d="M12 6v6l4 2"/></svg><div><small>Active</small><b>24 Hour</b></div></div>
<div class="abs pager"><svg width="12" height="20" viewBox="0 0 12 20"><path d="M10 2L2 10l8 8" fill="none" stroke="#1b2a31" stroke-width="3"/></svg><i></i><i></i><i></i><i></i><svg width="12" height="20" viewBox="0 0 12 20"><path d="M2 2l8 8-8 8" fill="none" stroke="#1b2a31" stroke-width="3"/></svg></div>

<!-- about -->
<div class="abs eyebrow">ABOUT</div>
<h2 class="abs about-title">Calm Harbor</h2>
<p class="abs about-text">Lorem ipsum dolor sit amet, consectetur adipiscing elit. Phasellus pretium metus sem, convallis laoreet lorem viverra id. Donec vitae pellenque leo, et feugiat lacus. Fusce vulputate, quam vitae sollicitudin facilisis, urna nisi porttitor neque, vel euismod orci massa ac enim. Curabitur ultrices a libero nec suscipit. Integer tortor dolor, tincidunt non ipsum at, blandit interdum magna. Phasellus ac lorem condimentum, efficitur metus vitae, porta est. Fusce massa quam, porttitor vel tortor non, porttitor ullamcorper ex. Nulla maximus turpis felis. Ut vel elit sed tellus pulvinar dictum.</p>
<form class="abs help">
  <h3>How Can We Help?</h3>
  <div class="field">First Name</div>
  <div class="field">Last Name</div>
  <div class="field">Email Address</div>
  <div class="submit">Submit</div>
</form>

<!-- offer -->
<section class="abs offer"></section>
<h2 class="abs offer-title">What We Can Offer</h2>
<p class="abs offer-sub">Vestibulum ante ipsum primis in faucibus orci luctus et ultrices posuere cubilia curae; Quisque in commodo odio, eu ultrices mi. Sed auctor ante mollis, viverra purus sit amet, iaculis eros.</p>
<div class="abs service" style="left:96px;top:1523px"><div class="pic" role="img" aria-label="Line illustration for relationships"></div><h4>Relationship</h4><p>Lorem ipsum dolor sit amet, consectetur adipiscing elit. Morbi dictum tempus urna, cursus ac</p></div>
<div class="abs service" style="left:440px;top:1523px"><div class="pic" role="img" aria-label="Line illustration for depression"></div><h4>Depression</h4><p>Lorem ipsum dolor sit amet, consectetur adipiscing elit. Morbi dictum tempus urna, cursus ac</p></div>
<div class="abs service" style="left:784px;top:1523px"><div class="pic" role="img" aria-label="Line illustration of puzzle pieces"></div><h4>Mind Game</h4><p>Lorem ipsum dolor sit amet, consectetur adipiscing elit. Morbi dictum tempus urna, cursus ac</p></div>
<div class="abs service" style="left:96px;top:1800px"><div class="pic" role="img" aria-label="Line illustration for conflict"></div><h4>Conflicting</h4><p>Lorem ipsum dolor sit amet, consectetur adipiscing elit. Morbi dictum tempus urna, cursus ac</p></div>
<div class="abs service" style="left:440px;top:1800px"><div class="pic" role="img" aria-label="Line illustration for mental health"></div><h4>Mental Health</h4><p>Lorem ipsum dolor sit amet, consectetur adipiscing elit. Morbi dictum tempus urna, cursus ac</p></div>
<div class="abs service" style="left:784px;top:1800px"><div class="pic" role="img" aria-label="Line illustration of a lotus for meditation"></div><h4>Meditation</h4><p>Lorem ipsum dolor sit amet, consectetur adipiscing elit. Morbi dictum tempus urna, cursus ac</p></div>

<!-- who we are -->
<h2 class="abs who-title">Who We Are</h2>
<p class="abs who-text">Curabitur ultrices a libero nec suscipit. Integer t dolor, tincidunt non ipsum at, blandit interdum msellus ac lorem condimentum, efficitur metus vitae, porta est. Cras eros est, iaculis nec nisi sed, hendrerit consequat tellus.</p>
<div class="abs stats">
  <div class="stat"><b>14K+</b><span>Happy Clients</span></div>
  <div class="stat"><b>+72%</b><span>Problem Solved</span></div>
  <div class="stat"><b>142+</b><span>Certified Expert</span></div>
</div>
<div class="abs photo" style="left:611px;top:2223px;width:486px;height:356px;background:linear-gradient(135deg,#e4e6e3,#c9cbc4 60%,#a69c8d)" role="img" aria-label="Therapy session in a bright room"></div>

<!-- video -->
<div class="abs video" role="img" aria-label="Video still of a woman resting calmly by a lake"></div>
<svg class="abs" style="left:535px;top:2895px" width="116" height="116" viewBox="0 0 116 116"><circle cx="58" cy="58" r="55" fill="rgba(255,255,255,.15)" stroke="#fff" stroke-width="4"/><path d="M45 34L85 58 45 82Z" fill="#fff"/></svg>
<svg class="abs" style="left:1048px;top:2720px" width="38" height="32" viewBox="0 0 24 20"><path d="M14 1l9 8-9 8v-5c-6 0-10 2-13 7 1-7 5-12 13-13z" fill="#fff"/></svg>

<!-- benefits -->
<h2 class="abs ben-title">Benefits of<br><em>Calm Harbor</em></h2>
<ul class="abs ben-list">
  <li>Tincidunt non ipsum at, blandit interdum msellus ac</li>
  <li>Lorem condimentum, efficitur metus vitae, porta est.</li>
  <li>Cras eros est, iaculis nec nisi sed, hendrerit consequat tellus.</li>
  <li>Phasellus lacinia quam dolor.</li>
</ul>
<div class="abs photo" style="left:611px;top:3367px;width:486px;height:357px;background:linear-gradient(135deg,#d5dbe0,#eef0f1 50%,#8a94a4)" role="img" aria-label="Counsellor talking with a client"></div>

<!-- testimonial -->
<div class="abs photo" style="left:100px;top:3848px;width:455px;height:484px;border-radius:12px;background:linear-gradient(135deg,#b9ad9c,#e2ddd5 40%,#6f6a5e)" role="img" aria-label="Group therapy session"></div>
<div class="abs quote-card">
  <svg width="42" height="34" viewBox="0 0 42 34"><path d="M2 2h16v16l-8 14H4l6-14H2zM24 2h16v16l-8 14h-6l6-14h-8z" fill="#0b5566"/></svg>
  <h3>What they Say</h3>
  <p>Lorem ipsum dolor sit amet, consectetur adipiscing elit. Phasellus pretium metus sem, convallis laoreet lorem viverra id. Donec vitae pellenque leo.</p>
  <div class="person"><div class="avatar" role="img" aria-label="Client portrait"></div><div><b>Daniel Reed</b><small>Patient</small></div></div>
</div>

<!-- footer -->
<footer class="abs footer"></footer>
<div class="abs meditate" role="img" aria-label="Woman meditating in a cross-legged pose"></div>
<div class="abs f-brand">Calm Harbor</div>
<p class="abs f-text">Lorem ipsum dolor sit at, consectetur adipiscing elit. Phasellus pretium metus sem, convallis laoreet lorem viverra id. Donec vitae pellenque leo,</p>
<div class="abs social foot" aria-label="Social links"><span></span><span></span><span></span></div>
<div class="abs f-links-title">Useful Links</div>
<ul class="abs f-links"><li>Terms and conditions</li><li>Privacy Policy</li></ul>
<div class="abs f-rule"></div>
<div class="abs copy">© 2023 <b>Calm Harbor</b>. All right reserved</div>

</body>
</html>
```